Business Card Design

I am selling Cruelty Free/not tested on animal products.
Ideally I would like pictures of rabbits/guinea pigs/Beagle(dog)/rat/mice, as these are the main creatures that are tested on.
Background of card Earth, clouds or rainbow.
Yes I am an animal activist.
My favorite colours are purple and green.

Reason: havent got the perfect design as yet

Industry/Entity Type

Business

Contact Information for Business Card

GENTLY BY NATURE
Cruelty Free Products
Norma Faldt
0492 837 514

```html
<!DOCTYPE html>
<html lang="en">
<head>
<meta charset="utf-8">
<title>Gently By Nature – Business Card</title>
<link rel="stylesheet" href="https://fonts.googleapis.com/css2?family=Cinzel:wght@500;600&family=Arimo:wght@400;700&display=swap">
<style>
  :root {
    --page-bg: #eeecf1;
    --sky-lilac: #c9b6dc;
    --sky-pink: #e6c9df;
    --sky-blue: #d9e4f3;
    --sky-white: #f7f4fb;
    --sky-violet: #8f78b8;
    --brand-purple: #5a2d86;
    --brand-green: #1d8a3c;
    --phone-purple: #4a3278;
    --band-white: rgba(255, 255, 255, 0.55);
    --band-edge: rgba(255, 255, 255, 0.8);
  }

  html, body {
    margin: 0;
    padding: 0;
    width: 1200px;
    height: 900px;
    overflow: hidden;
    background: var(--page-bg);
  }

  .canvas {
    position: relative;
    width: 1200px;
    height: 900px;
  }

  .business-card {
    position: absolute;
    left: 100px;
    top: 140px;
    width: 1000px;
    height: 620px;
    border-radius: 30px;
    overflow: hidden;
    box-shadow: 0 18px 40px rgba(60, 40, 90, 0.18);
  }

  .cloud-sky {
    position: absolute;
    inset: 0;
    background:
      radial-gradient(ellipse 40% 30% at 20% 35%, var(--sky-white) 0%, rgba(247,244,251,0) 70%),
      radial-gradient(ellipse 45% 28% at 75% 55%, var(--sky-white) 0%, rgba(247,244,251,0) 70%),
      radial-gradient(ellipse 50% 25% at 40% 75%, rgba(255,255,255,0.85) 0%, rgba(255,255,255,0) 70%),
      radial-gradient(ellipse 40% 30% at 85% 10%, var(--sky-blue) 0%, rgba(217,228,243,0) 70%),
      linear-gradient(180deg, #e4ddef 0%, var(--sky-pink) 35%, var(--sky-lilac) 60%, #e9e0f1 80%, var(--sky-violet) 100%);
  }

  .animal-lineup {
    position: absolute;
    left: 300px;
    top: 130px;
    width: 560px;
    height: 150px;
    border-radius: 60px 60px 14px 14px;
    background: linear-gradient(90deg, #d8c6b0 0%, #e0b27a 30%, #9c8f86 58%, #6a4a35 78%, #f2eee8 100%);
    opacity: 0.9;
  }

  .brand {
    position: absolute;
    left: 0;
    right: 0;
    top: 282px;
    text-align: center;
  }

  .brand-name {
    margin: 0;
    font-family: "Cinzel", serif;
    font-weight: 600;
    font-size: 58px;
    line-height: 1;
    letter-spacing: 1px;
    color: var(--brand-purple);
  }

  .brand-tagline {
    margin: 8px 0 0;
    font-family: "Arimo", sans-serif;
    font-weight: 700;
    font-size: 33px;
    letter-spacing: 3px;
    color: var(--brand-green);
  }

  .contact-band {
    position: absolute;
    left: 0;
    right: 0;
    top: 410px;
    height: 110px;
    background: var(--band-white);
    border-top: 2px solid var(--band-edge);
    border-bottom: 2px solid var(--band-edge);
    text-align: center;
  }

  .base-band {
    position: absolute;
    left: 0;
    right: 0;
    top: 522px;
    height: 98px;
    background: linear-gradient(180deg, rgba(143,120,184,0.35), rgba(120,96,170,0.55));
  }

  .contact-name {
    margin: 18px 0 0;
    font-family: "Arimo", sans-serif;
    font-weight: 400;
    font-size: 36px;
    color: var(--brand-green);
  }

  .contact-phone {
    margin: 8px 0 0;
    font-family: "Arimo", sans-serif;
    font-weight: 400;
    font-size: 36px;
    letter-spacing: 1px;
    color: var(--phone-purple);
  }
</style>
</head>
<body>
<main class="canvas">
  <section class="business-card">
    <div class="cloud-sky" role="img" aria-label="Soft pastel sky full of pink, lilac and white clouds"></div>
    <div class="animal-lineup" role="img" aria-label="Row of animals sitting side by side: a lop-eared rabbit, a guinea pig, a grey mouse and a beagle puppy"></div>
    <div class="brand">
      <h1 class="brand-name">GENTLY BY NATURE</h1>
      <p class="brand-tagline">Cruelty Free Products</p>
    </div>
    <div class="contact-band">
      <p class="contact-name">Norma Faldt</p>
      <p class="contact-phone">0492 837 514</p>
    </div>
    <div class="base-band"></div>
  </section>
</main>
</body>
</html>
```